Coach/consultant in conflict and challenge needs an enticing flyer

I need a double sided DL flyer design that will describe my work in helping people meet conflict and emotional challenge so they can learn and grow from these difficulties. I want to give a flavour of my style through fresh colours, repeated images used differently (the spiral), and a sense of positivity around conflict and difficulty. I want to attract people who are keen to do things differently and want to engage with creative processes rather than getting stuck in familiar patterns. My work is creative and often includes use of story, images and fables, so I want to convey that as well. I also place the work in a spiritual context, but grounded in practicality so I don't want it to seem New Age or flakey. I want something that seems innovative, professional and intriguing. I've included a sample of something I mocked up in word and also a copy of a flyer for Mirela Tasker's Hearthbound Rite that inspired me to get a DL flyer. I want the design to communicate trust and transformation and engaging with fresh ways of doing things by moving past old habits

Target Market(s)

Mid 30s plus women and men who want to change their approach to conflict and emotional difficulties and are willing to take the creative and challenging journey to do that

Industry/Entity Type

Learn

Colors
acd136
00a990

Requirements
Must have
• a shift in the use of the spiral image,
• use of image of me (Moira)
• bright fresh colours olours that represent growth and transformation--I've suggested lime green as it suggests a sense of growth
• easy to read text
Nice to have
• Interesting non-traditional fonts perhaps text in a contemporary sans serif and another brush script font (like the Hearthbound Rite example)
• bleed to the edge and run off the page images or text
Should not have
• anything that represents too much tradition or stuckness

```html
<!DOCTYPE html>
<html lang="en">
<head>
<meta charset="utf-8">
<title>Moira Calloway – DL Flyer</title>
<link href="https://fonts.googleapis.com/css2?family=Caveat+Brush&family=Mulish:ital,wght@0,700;0,800;1,700&family=Questrial&display=swap" rel="stylesheet">
<style>
  :root {
    --bg: #ecece6;
    --lime: #9cbf1e;
    --lime-light: #b3d24a;
    --forest: #4b6b17;
    --forest-deep: #3f5c12;
    --olive-text: #4a5d14;
    --muted: #5f7a1c;
    --white: #ffffff;
  }
  * { box-sizing: border-box; margin: 0; padding: 0; }
  html, body { width: 1067px; height: 1200px; overflow: hidden; background: var(--bg); }
  .canvas { position: relative; width: 1067px; height: 1200px; }

  .panel {
    position: absolute; left: 58px; width: 964px; height: 506px;
    background: var(--lime); overflow: hidden;
  }
  .panel--front { top: 85px; }
  .panel--back { top: 620px; }

  .spiral-mark { position: absolute; border-radius: 50%; }
  .panel--front .spiral-halo {
    left: -110px; top: -70px; width: 560px; height: 560px;
    background: radial-gradient(circle, rgba(179,210,74,0.5) 0%, rgba(179,210,74,0.25) 50%, rgba(156,191,30,0) 70%);
  }
  .panel--front .spiral-main {
    left: 38px; top: 33px; width: 280px; height: 280px;
    background: radial-gradient(circle, rgba(75,107,23,0.75) 0%, rgba(75,107,23,0.55) 45%, rgba(75,107,23,0) 72%);
  }

  .brand-name {
    position: absolute; left: 366px; top: 62px;
    font-family: "Caveat Brush", cursive; font-size: 88px; font-weight: 400; line-height: 1;
    color: var(--white); letter-spacing: 1px;
  }
  .values {
    position: absolute; left: 375px; top: 162px; display: flex; gap: 40px;
    font-family: "Caveat Brush", cursive; font-size: 36px; color: var(--forest-deep);
  }
  .values span::before { content: "# "; font-size: 20px; }

  .intro {
    position: absolute; left: 367px; top: 251px; width: 548px;
    font-family: "Questrial", sans-serif; font-size: 22.5px; line-height: 26px; color: var(--white);
  }
  .tagline {
    position: absolute; left: 367px; top: 388px; width: 560px;
    font-family: "Mulish", sans-serif; font-style: italic; font-weight: 700;
    font-size: 20px; line-height: 26px; color: var(--olive-text);
  }

  .portrait-frame { position: absolute; left: 0; top: 0; width: 370px; height: 506px; }

  .about {
    position: absolute; left: 378px; top: 33px; width: 335px;
    font-family: "Questrial", sans-serif; font-size: 16px; line-height: 19.5px; color: var(--white);
  }
  .about p + p { margin-top: 19px; }

  .services {
    position: absolute; left: 731px; top: 30px; width: 230px; list-style: none;
    font-family: "Caveat Brush", cursive; font-size: 42px; line-height: 57px;
    color: var(--forest-deep); text-align: center;
  }

  .panel--back .spiral-faint {
    right: -30px; bottom: -50px; width: 240px; height: 240px;
    background: radial-gradient(circle, rgba(120,160,25,0.55) 0%, rgba(120,160,25,0.35) 45%, rgba(156,191,30,0) 70%);
  }

  .contact { position: absolute; left: 378px; top: 328px; width: 540px; }
  .contact-name {
    font-family: "Mulish", sans-serif; font-weight: 800; font-size: 27px; color: var(--olive-text);
  }
  .credentials {
    margin-top: 4px; font-family: "Questrial", sans-serif; font-size: 18px; color: var(--muted);
  }
  .contact-grid {
    margin-top: 18px; display: grid; grid-template-columns: 220px 18px auto; column-gap: 5px; row-gap: 4px;
    font-family: "Mulish", sans-serif; font-weight: 700; font-size: 17.5px; color: var(--white);
  }
  .contact-grid .sep { text-align: center; }
  .abn {
    margin-top: 12px; font-family: "Mulish", sans-serif; font-weight: 700; font-size: 14px; color: var(--white);
  }
</style>
</head>
<body>
<main class="canvas">

  <section class="panel panel--front">
    <div class="spiral-mark spiral-halo" role="img" aria-label="Large faint brush-painted spiral sweeping off the panel edge"></div>
    <div class="spiral-mark spiral-main" role="img" aria-label="Dark green hand-brushed spiral"></div>

    <h1 class="brand-name">Moira Calloway</h1>
    <p class="values"><span>courage</span><span>listening</span><span>creativity</span></p>

    <p class="intro">Challenge, change and conflict are a natural part of life. When we greet them with courage, and listen to what they tell us, we grow in wisdom, resilience and creativity.</p>
    <p class="tagline">Moira Calloway is a coach, educator and mediator. She works with people who want to harvest the fruits of challenge and conflict so they can live life differently.</p>
  </section>

  <section class="panel panel--back">
    <svg class="portrait-frame" viewBox="0 0 370 506" width="370" height="506">
      <defs>
        <linearGradient id="portraitTone" x1="0" y1="0" x2="0" y2="1">
          <stop offset="0" stop-color="#9a958e"/>
          <stop offset="0.35" stop-color="#d6a58c"/>
          <stop offset="0.65" stop-color="#d8581f"/>
          <stop offset="1" stop-color="#c24a17"/>
        </linearGradient>
      </defs>
      <path d="M0 0 H280 C350 70 368 190 360 280 C350 400 260 480 60 506 H0 Z" fill="#3f5c12" aria-hidden="true"/>
      <path d="M0 0 H130 C225 55 264 160 258 280 C252 380 185 455 0 500 Z"
            fill="url(#portraitTone)" role="img" aria-label="Portrait photograph of Moira in an orange knitted wrap"/>
    </svg>

    <div class="about">
      <p>Consult with Moira to address challenges in your life, relationship, group or organisation. Through listening, conversation and creative processes, you will discover what your challenge is asking of you. Moira is a skilled facilitator who works to shift people’s responses from reactivity to creativity.</p>
      <p>With many years’ experience in coaching and mentorship, mediation and narrative processes, Moira supports you to discover authentic responses to difficult situations.</p>
    </div>

    <ul class="services">
      <li>consultations</li>
      <li>workshops</li>
      <li>speaking</li>
      <li>writing</li>
    </ul>

    <div class="spiral-mark spiral-faint" role="img" aria-label="Faint brush-painted spiral"></div>

    <div class="contact">
      <h2 class="contact-name">Moira Calloway</h2>
      <p class="credentials">PhD, MCR, BAppSci, DipHum, AssDipEd</p>
      <div class="contact-grid">
        <span>0400 555 218 (m)</span><span class="sep">|</span><span>+61 3 9000 4417 (h)</span>
        <span>moira@moiracalloway.com</span><span class="sep">|</span><span>moiracalloway.com</span>
      </div>
      <p class="abn">ABN 00 000 111 22</p>
    </div>
  </section>

</main>
</body>
</html>
```